Need a landing page design.

We are currently trying to develop a landing page for our www.brightoakwellness.example website.

Objective: To peak a level of interest in Medical Practices to sign up to our program and promote our line of vitamins and supplements. We will be concentrating on email marketing as well as fax or direct mail to drive medical facilities to our landing page.

Page requirements:
1. A slider on the top portion showing our line of products from the brightoakwellness.example website.
2. An "about us" area to explain who we are and what we offer.
3. An area for a grid so that we can show potential earnings for the practice as part of our program.
4. A Testimonial area for a couple of testimonials
5. A scroll area where they can see our contract
6. A lead capture area where they can input their contact information so we may gather it and contact them back to explain the program. In this area I need the following fields: Name of Practice; Contact name; Email address; Phone Number; Area of Medical Discipline; Number of patients per day.
7. A nice clean contact us area

Other than these main requirements the rest is up to you.

Goal: Entice Medical practices to use our FREE service to increase revenue for their offices while helping their patients save money on their supplements.

Key Factors for the Medical facility to know: Free to sign up, no inventory carrying costs. Simple backend sales area to process orders. We handle all shipping and customer service.

Thank you

Target Market(s)

Medical Facilities, mainly office managers and docotors

Industry/Entity Type

Marketing

Requirements
Must have
• Professional design as we are dealing with the medical field.

```html
<!DOCTYPE html>
<html lang="en">
<head>
<meta charset="utf-8">
<title>Bright Oak Wellness – Practice Program</title>
<link href="https://fonts.googleapis.com/css2?family=Montserrat:wght@400;600;700&family=Oswald:wght@500&family=Roboto:wght@400;700&family=Tinos:wght@400&display=swap" rel="stylesheet">
<style>
:root{
  --teal:#5cc4cc;
  --teal-dark:#3fa9b3;
  --brown:#7a5b43;
  --brown-top:#6b4f3a;
  --page:#efefef;
  --band:#e2e2e2;
  --ink:#222;
  --line:#d4d4d4;
  --red:#e23a3a;
  --grey-btn:#a3a3a3;
}
*{box-sizing:border-box;margin:0;padding:0}
html,body{width:674px;height:1200px;overflow:hidden}
body{position:relative;background:var(--page);font-family:"Roboto",Arial,sans-serif;color:var(--ink);font-size:7px;border-top:3px solid var(--brown-top);
  background-image:radial-gradient(#e6e6e6 1px,transparent 1.2px);background-size:6px 6px}
.abs{position:absolute}
/* header */
.brand{left:88px;top:12px;display:flex;align-items:center;gap:8px}
.brand-mark{width:58px;height:58px;border-radius:50%;background:var(--teal);border:3px solid #d9eff1}
.brand-name{font-family:"Montserrat",sans-serif;font-weight:600;font-size:12px;color:var(--teal-dark)}
.toplinks{left:366px;top:17px;font-size:7px;display:flex;gap:6px;color:#333;align-items:center}
.toplinks .sep{color:#666}
.inquiries{left:440px;top:33px;text-align:right;font-size:7px;line-height:10px;width:78px}
.tools{left:529px;top:34px;display:flex;gap:3px}
.tools span{background:#222;color:#fff;height:17px;min-width:18px;font-size:6.5px;display:flex;align-items:center;justify-content:center;font-weight:700}
.nav{left:88px;top:82px;width:500px;height:30px;background:#fff;border:1px solid var(--line)}
.nav .home{position:absolute;left:0;top:-1px;width:51px;height:30px;border-top:3px solid var(--teal);display:flex;align-items:center;justify-content:center;border-right:1px solid var(--line)}
.nav a{position:absolute;top:10px;font-size:7.5px;color:#333;text-decoration:none}
.nav .div{position:absolute;top:0;width:1px;height:28px;background:var(--line)}
.search{position:absolute;left:362px;top:8px;width:95px;height:14px;border:1px solid var(--line);font-size:4.5px;color:#bbb;padding:4px 4px}
.search-btn{position:absolute;left:457px;top:8px;width:38px;height:14px;background:var(--teal);display:flex;align-items:center;justify-content:center}
/* slider */
.slider{left:87px;top:126px;width:501px;height:181px;background:#fff;border:1px solid var(--line)}
.banner-red{left:106px;top:136px;width:305px;height:145px;overflow:hidden;background:radial-gradient(circle at 75% 45%,#d9403d,#a61f1f 55%,#7e1414)}
.banner-red h2{position:absolute;left:9px;top:8px;font-family:"Oswald",sans-serif;font-weight:500;font-size:15.5px;color:#fff;z-index:2;white-space:nowrap}
.banner-red ul{position:absolute;left:10px;top:37px;list-style:none;color:#fff;font-weight:700;font-size:6.8px;line-height:13.4px;z-index:2}
.banner-red li::before{content:"✓";margin-right:5px}
.shop{position:absolute;left:12px;top:119px;width:106px;height:17px;background:var(--red);border-radius:3px 9px 9px 3px;color:#fff;font-weight:700;font-size:8px;display:flex;align-items:center;justify-content:center;box-shadow:0 1px 0 #7e1414}
.product-tub{position:absolute;left:208px;top:12px;width:88px;height:126px;border-radius:14px;background:radial-gradient(circle at 35% 30%,#ffffff,#e3e8df 45%,#b9c4b3);box-shadow:0 3px 8px rgba(0,0,0,.35)}
.banner-blue{left:419px;top:136px;width:151px;height:145px;background:linear-gradient(#3584cc,#1b4f94);font-family:"Tinos",serif;color:#fff;text-align:center;overflow:hidden}
.banner-blue .t1{margin-top:6px;font-size:8px}
.banner-blue .t2{font-size:10.5px}
.banner-blue .bottles{margin:6px auto 0;width:120px;height:80px;border-radius:6px;background:radial-gradient(ellipse at 50% 45%,#6fd0f2,#2a8cc8 55%,#1b5c98)}
.banner-blue .t3{margin-top:12px;font-size:8px}
.arrow{font-size:16px;font-weight:700;color:#111}
.dots{left:298px;top:291px;display:flex;gap:4px}
.dots i{width:5px;height:5px;border-radius:50%;background:#111;display:block}
.dots i.on{background:var(--teal)}
/* about */
.photo{background:linear-gradient(135deg,#f4f7f8 0%,#e3ecee 45%,#b9cdd2 100%);border:1px solid var(--teal);box-shadow:inset 0 0 0 3px #fff}
.sec-title{font-family:"Montserrat",sans-serif;font-weight:600;font-size:14px;color:var(--ink);white-space:nowrap}
.sec-title span{color:var(--teal);font-weight:400}
.sub{color:#c4c4c4;font-size:6px;line-height:7px}
.body{font-family:"Montserrat",sans-serif;font-size:5.6px;line-height:10px;text-align:justify;color:#222}
.body a{color:var(--teal);text-decoration:none}
.rule{height:1px;background:var(--line)}
/* form */
.field{left:415px;width:145px;height:18px;background:#fff;border:1px solid var(--line);font-family:"Montserrat",sans-serif;font-size:6px;color:#aaa;padding:5px 6px}
.btn{height:17px;background:var(--teal);color:#fff;font-family:"Montserrat",sans-serif;font-size:7px;display:flex;align-items:center;justify-content:center}
/* products */
.card{top:598px;width:109px;height:121px;background:#fff;border:1px solid var(--line)}
.card .shot{position:absolute;left:8px;top:8px;width:91px;height:103px}
.p-name{font-family:"Montserrat",sans-serif;font-weight:600;font-size:9.5px;color:var(--teal)}
.stars{color:#e8702a;font-size:7px;letter-spacing:1px}
.price{font-size:6.5px;line-height:10.5px}
.price b{font-weight:400;color:var(--red)}
.mini{height:14px;font-size:6.5px;color:#fff;display:flex;align-items:center;justify-content:center}
/* services */
.band{left:0;top:806px;width:674px;height:202px;background:var(--band)}
.ring{left:96px;top:812px;width:176px;height:176px;border-radius:50%;background:#f6f6f6;box-shadow:0 1px 4px rgba(0,0,0,.12)}
.portrait{left:104px;top:820px;width:160px;height:160px;border-radius:50%;background:radial-gradient(circle at 60% 45%,#f8e4d3,#e7bf9c 45%,#c99868 75%,#9a7551)}
.best{left:287px;top:826px;font-family:"Montserrat",sans-serif;line-height:24px}
.best .b1{color:var(--teal);font-size:22px;font-weight:400}
.best .b2{color:#444;font-size:22px;font-weight:700}
.best .b3{color:#777;font-size:20px;font-weight:600}
.serv-big{left:287px;top:901px;color:#999;font-size:13.5px;line-height:18px}
.serv-small{left:287px;top:944px;color:#666;font-size:7px;line-height:9.5px}
.badge{width:40px;height:40px;border-radius:50%;background:#666;border:3px solid #ddd;color:#fff;font-family:"Montserrat",sans-serif;font-size:18px;font-weight:700;display:flex;align-items:center;justify-content:center}
.serv-h{font-family:"Montserrat",sans-serif;font-weight:600;font-size:8.5px;color:#444;letter-spacing:.3px}
.serv-p{font-size:6.5px;color:#999;line-height:9.5px}
/* footer */
.footer{left:0;top:1008px;width:674px;height:192px;background:var(--brown);color:#fff}
.f-h{font-family:"Montserrat",sans-serif;font-size:10.5px;color:#fff}
.f-t{font-size:5.4px;line-height:9px;color:#f3ece6}
.f-t .tag{color:#9fe1e6}
.pay{width:19px;height:12px;border-radius:2px;border:1.5px solid #fff}
.seal{border-radius:50%;background:radial-gradient(circle,#f2cf55,#c8951d);border:3px dotted #f5dc7d;box-shadow:0 0 0 2px #b8841a}
.cert{background:#fff;padding:4px}
.cert div{width:100%;height:100%;border:2px solid #8fb54a;background:#eef5e0}
.social{width:17px;height:17px;border-radius:50%;border:2px solid rgba(255,255,255,.8)}
</style>
</head>
<body>

<!-- header -->
<div class="abs brand"><div class="brand-mark"></div><div class="brand-name">Bright Oak Wellness</div></div>
<div class="abs toplinks">
  <svg width="7" height="8" viewBox="0 0 7 8"><circle cx="3.5" cy="2" r="2" fill="#222"/><path d="M0 8a3.5 3.5 0 0 1 7 0z" fill="#222"/></svg><span>My Account</span><span class="sep">|</span>
  <svg width="9" height="7" viewBox="0 0 9 7"><path d="M0 .5h2l1 4h5l1-3H2.5" stroke="#222" fill="none"/><circle cx="3.5" cy="6.2" r=".8" fill="#222"/><circle cx="7" cy="6.2" r=".8" fill="#222"/></svg><span>Checkout</span><span class="sep">|</span>
  <span>Log In</span>
  <svg width="11" height="9" viewBox="0 0 9 7"><path d="M0 .5h2l1 4h5l1-3H2.5" stroke="#222" fill="none" stroke-width="1.2"/><circle cx="3.5" cy="6.2" r=".8" fill="#222"/><circle cx="7" cy="6.2" r=".8" fill="#222"/></svg><span>View Cart <span style="color:#aaa;font-size:5px">(empty)</span></span>
</div>
<div class="abs inquiries">General Inquiries<br>(555) 014-2290</div>
<div class="abs tools"><span>En ▾</span><span>$ ▾</span><span>
  <svg width="9" height="10" viewBox="0 0 9 10"><rect x="1" y="4" width="7" height="6" fill="#fff"/><path d="M2.5 4V2.5a2 2 0 0 1 4 0V4" stroke="#fff" fill="none" stroke-width="1.2"/></svg></span></div>

<nav class="abs nav">
  <div class="home"><svg width="11" height="10" viewBox="0 0 11 10"><path d="M5.5 0 0 5h1.5v5h3V7h2v3h3V5H11z" fill="#5cc4cc"/></svg></div>
  <a style="left:73px">Home</a>
  <div class="div" style="left:127px"></div>
  <a style="left:146px">About Us</a>
  <div class="div" style="left:229px"></div>
  <a style="left:239px">Contact Us</a>
  <div class="search">Type here...</div>
  <div class="search-btn"><svg width="12" height="10" viewBox="0 0 12 10"><circle cx="4" cy="4" r="3" stroke="#fff" stroke-width="1.4" fill="none"/><path d="M6.5 6 11 9" stroke="#fff" stroke-width="1.6"/></svg></div>
</nav>

<!-- slider -->
<section class="abs slider"></section>
<div class="abs banner-red">
  <h2>Increase Sex Drive &amp; Stamina</h2>
  <ul>
    <li>Helps Weight Control</li>
    <li>Helps Increase Energy</li>
    <li>Helps increase sex drive in men and women</li>
    <li>Helps improve hear health</li>
    <li>Helps increase muscle mass</li>
    <li>Helps improve stamina and vigor</li>
  </ul>
  <div class="shop">SHOP NOW</div>
  <div class="product-tub" role="img" aria-label="Supplement tub product photo"></div>
</div>
<div class="abs banner-blue">
  <div class="t1">Bright Oak Wellness</div>
  <div class="t2">Engineered For Quality</div>
  <div class="bottles" role="img" aria-label="Blue supplement bottles product photo"></div>
  <div class="t3">Choose The Right Product For You!</div>
</div>
<div class="abs arrow" style="left:93px;top:188px">‹</div>
<div class="abs arrow" style="left:574px;top:194px">›</div>
<div class="abs dots"><i></i><i></i><i class="on"></i><i></i><i></i></div>

<!-- about -->
<div class="abs photo" style="left:87px;top:325px;width:68px;height:102px" role="img" aria-label="Doctor holding a piggy bank"></div>
<div class="abs" style="left:175px;top:323px;width:200px">
  <div class="sec-title">About <span>Us</span></div>
  <div class="sub" style="margin-top:2px;width:90px">Resume your active and healthy lifestyle</div>
  <div class="rule" style="width:88px;margin-top:2px"></div>
</div>
<p class="abs body" style="left:175px;top:367px;width:199px">Mauris pulvinar lectus ac nulla consectetur cursus. Suspendisse viverra eros vel ante vehicula elementum.Pellentesque habitant morbi tristique senectus et netus et malesuada fames ac turpis egestas. Pellentesque habitant morbi tristique senectus et netus et malesuada fames ac turpis egestas. Donec aliquet posuere vulputate <a>Read More</a></p>

<div class="abs photo" style="left:87px;top:441px;width:68px;height:102px" role="img" aria-label="Doctor holding a piggy bank"></div>
<div class="abs" style="left:175px;top:442px;width:200px">
  <div class="sec-title" style="font-size:12.5px">Earning For the <span>Practice</span></div>
  <div class="sub" style="margin-top:2px">Mauris eget diam nibh, at sollicitudin nunc</div>
  <div class="rule" style="width:140px;margin-top:1px"></div>
</div>
<p class="abs body" style="left:175px;top:476px;width:197px">Pellentesque habitant morbi tristique senectus et netus et malesuada fames ac turpis egestas. Donec aliquet posuere vulputate. Aliquam malesuada tortor quis magna pretium sit amet rhoncus risus pretium. Phasellus interdum bibendum purus, ac venenatis orci egestas. <a>Read More</a></p>

<!-- lead capture -->
<div class="abs" style="left:415px;top:326px;width:172px">
  <div class="sec-title" style="font-size:12.5px">Contact <span>Information</span></div>
  <div class="sub">Lorem ipsum dolor</div>
  <div class="rule" style="margin-top:2px"></div>
</div>
<div class="abs field" style="top:364px">Name Of Practice</div>
<div class="abs field" style="top:387px">Contact Name</div>
<div class="abs field" style="top:411px">Email Address</div>
<div class="abs field" style="top:436px">Phone</div>
<div class="abs field" style="top:462px">Area Of Medical Discipline</div>
<div class="abs field" style="top:488px">No.of Patients Per Day</div>
<div class="abs btn" style="left:417px;top:523px;width:55px">Submit</div>
<div class="abs btn" style="left:504px;top:523px;width:55px">Clear</div>

<!-- contracts -->
<div class="abs" style="left:87px;top:565px;font-family:'Montserrat',sans-serif;font-weight:600;font-size:11.5px">Our Contracts</div>
<div class="abs rule" style="left:87px;top:584px;width:138px;background:#c8c8c8"></div>
<svg class="abs" style="left:72px;top:634px" width="24" height="26" viewBox="0 0 24 26"><path d="M20 2 6 13l14 11" stroke="#111" stroke-width="5" fill="none"/></svg>
<svg class="abs" style="left:576px;top:638px" width="24" height="26" viewBox="0 0 24 26"><path d="M4 2l14 11L4 24" stroke="#111" stroke-width="5" fill="none"/></svg>

<div class="abs card" style="left:101px"><div class="shot" role="img" aria-label="Chocolate shake canister" style="background:radial-gradient(ellipse at 50% 45%,#d8cfc3,#a08c78 55%,#fff 80%)"></div></div>
<div class="abs card" style="left:220px"><div class="shot" role="img" aria-label="Dark supplement bottle" style="background:radial-gradient(ellipse at 50% 45%,#4a5262,#1a1f29 55%,#fff 80%)"></div></div>
<div class="abs card" style="left:339px"><div class="shot" role="img" aria-label="Blue supplement bottle" style="background:radial-gradient(ellipse at 50% 45%,#62c2ec,#1f78b4 55%,#fff 80%)"></div></div>
<div class="abs card" style="left:458px"><div class="shot" role="img" aria-label="White supplement bottle" style="background:radial-gradient(ellipse at 50% 45%,#ffffff,#c9d1e0 55%,#fff 80%)"></div></div>

<div class="abs" style="left:114px;top:726px">
  <div class="p-name">Eagation Shake</div><div class="stars">★★★★★</div>
  <div class="price">Easy Auto Ship: <b>$33.25</b><br>Regular Price: <b>$39.95</b></div>
</div>
<div class="abs" style="left:234px;top:724px">
  <div class="p-name">Eagation Shake</div><div class="stars">★★★★★</div>
  <div class="price">Easy Auto Ship: <b>$33.25</b><br>Regular Price: <b>$39.95</b></div>
</div>
<div class="abs" style="left:350px;top:724px">
  <div class="p-name">Eagation Shake</div><div class="stars">★★★★★</div>
  <div class="price">Easy Auto Ship: <b>$33.25</b><br>Regular Price: <b>$39.95</b></div>
</div>
<div class="abs" style="left:467px;top:724px">
  <div class="p-name">Eagation Shake</div><div class="stars">★★★★★</div>
  <div class="price">Easy Auto Ship: <b>$33.25</b><br>Regular Price: <b>$39.95</b></div>
</div>
<div class="abs mini" style="left:114px;top:773px;width:37px;background:var(--teal)">Add</div>
<div class="abs mini" style="left:157px;top:773px;width:38px;background:var(--grey-btn)">Details</div>
<div class="abs mini" style="left:233px;top:772px;width:37px;background:var(--teal)">Add</div>
<div class="abs mini" style="left:276px;top:772px;width:38px;background:var(--grey-btn)">Details</div>
<div class="abs mini" style="left:350px;top:772px;width:37px;background:var(--teal)">Add</div>
<div class="abs mini" style="left:394px;top:772px;width:38px;background:var(--grey-btn)">Details</div>
<div class="abs mini" style="left:466px;top:772px;width:37px;background:var(--teal)">Add</div>
<div class="abs mini" style="left:510px;top:772px;width:38px;background:var(--grey-btn)">Details</div>

<!-- services -->
<section class="abs band"></section>
<div class="abs ring"></div>
<div class="abs portrait" role="img" aria-label="Smiling woman portrait"></div>
<div class="abs best"><div class="b1">BEST</div><div class="b2">Services</div><div class="b3">For You!</div></div>
<div class="abs serv-big">Meciegast nverstaese<br>saeitset ertplica.</div>
<div class="abs serv-small">Meuctus aloecase magna oncumsan eras<br>maleasit onuris fermen.</div>
<div class="abs badge" style="left:432px;top:837px">A</div>
<div class="abs badge" style="left:439px;top:916px">B</div>
<div class="abs" style="left:491px;top:833px">
  <div class="serv-h">SHIPPING SERVICES</div>
  <div class="serv-p" style="margin-top:5px">Matsearit masertas lertydes<br>aplicabo nerafaes lasertyus<br>ertyasnemo.</div>
</div>
<div class="abs rule" style="left:491px;top:892px;width:100px"></div>
<div class="abs" style="left:495px;top:914px">
  <div class="serv-h">BEST OFFERS</div>
  <div class="serv-p" style="margin-top:5px">Kyatrsas asertas lmoiasas<br>paset aplicabo nerlaserytus<br>tyasnem ersvitae ero.</div>
</div>
<div class="abs" style="left:494px;top:984px;font-size:7.5px;font-weight:700;color:#333">• view more info</div>

<!-- footer -->
<footer class="abs footer">
  <svg class="abs" style="left:88px;top:14px" width="20" height="20" viewBox="0 0 20 20"><rect x="1" y="3" width="13" height="15" fill="#3d7fc2"/><path d="M6 14 18 2" stroke="#e0463e" stroke-width="3"/></svg>
  <div class="abs f-h" style="left:113px;top:21px">Testimonial</div>
  <p class="abs f-t" style="left:88px;top:50px;width:152px"><b>Lorem Ipsum is simply dummy text of the printing and typesetting industry.</b> Lorem Ipsum has been the industry's standard dummy text ever since the 1500s, when an unknown printer</p>
  <p class="abs f-t" style="left:88px;top:96px;width:152px">Took a galley of type and scrambled it to make a type specimen book. It has survived not only five centuries, but also<br><span class="tag">Read more &gt;&gt;</span></p>
  <div class="abs f-h" style="left:88px;top:138px">We Accept:</div>
  <div class="abs pay" style="left:88px;top:154px;background:#2c5fb3"></div>
  <div class="abs pay" style="left:111px;top:154px;background:#e0663a"></div>
  <div class="abs pay" style="left:134px;top:154px;background:#7fb8e6"></div>
  <div class="abs pay" style="left:157px;top:154px;background:#3e7bc4"></div>
  <div class="abs seal" style="left:193px;top:143px;width:46px;height:46px"></div>
  <div class="abs cert" style="left:250px;top:142px;width:68px;height:42px"><div></div></div>
  <div class="abs cert" style="left:328px;top:142px;width:56px;height:42px"><div style="border-color:#3a8f5a;background:#e2f1e7"></div></div>

  <svg class="abs" style="left:254px;top:16px" width="18" height="18" viewBox="0 0 18 18"><path d="M1 5 12 1l5 11-11 5z" fill="#e8c63b"/><path d="M1 5l8 5 8-8" stroke="#b8961b" fill="none"/></svg>
  <div class="abs f-h" style="left:275px;top:19px">Contact us</div>
  <p class="abs f-t" style="left:255px;top:50px;width:110px">Firm: ABC Address: 123 abcstreet<br>Address: 123 abcstreet,<br>25 City Address: 123 abcstreet,<br><span class="tag">Phone :</span> +123 123123, +123 123 123<br><span class="tag">Fax :</span> +12345678<br><span class="tag">Email :</span> info@brightoakwellness.example<br><span class="tag">Website :</span> brightoakwellness.example</p>

  <div class="abs f-h" style="left:362px;top:19px">Quick links</div>
  <p class="abs f-t" style="left:362px;top:50px;line-height:10px">Home<br>About Us<br>Products<br>Contact Us<br>Become an Affiliate<br>Become an Reseller</p>

  <div class="abs f-h" style="left:468px;top:19px">Terms and Conditions</div>
  <p class="abs f-t" style="left:469px;top:46px;line-height:10.5px">Privacy Policy<br>Return Policy<br>Terms and Conditions</p>

  <div class="abs f-h" style="left:438px;top:159px;font-size:10px;letter-spacing:.5px">Follow on:</div>
  <div class="abs social" style="left:500px;top:156px;background:#3b5b9a"></div>
  <div class="abs social" style="left:524px;top:156px;background:#d9473a"></div>
  <div class="abs social" style="left:547px;top:156px;background:#cc2020"></div>
  <div class="abs social" style="left:570px;top:156px;background:#3fa9e0"></div>
  <div class="abs f-t" style="left:438px;top:182px;font-size:5.5px">© Copyright 2013. All rights reserved.</div>
</footer>

</body>
</html>
```